Adventskalender
Zielgruppe
Männer im Alter zwischen 29 u. 49 Jahren, hohe Bildung, höheres Einkommen, sehr modeaffin.
Varos-Segmente: Moderne Performer, Postmateriell und Etablierte.
Aufgabenstellung
Wir wünschen uns die Gestaltung eines Adventskalenders, den wir im Dezember im Rahmen einer Aktion auf unseren Seiten verwenden möchten.
Gestaltet werden sollen zwei Typen von Seiten (siehe Screenshots):
1. Adventskalender
2. Detailseite nach Klick auf ein Türchen mit Gewinn und der Aufgabe für diesen Tag

```html
<!DOCTYPE html>
<html lang="de">
<head>
<meta charset="utf-8">
<title>Online Adventskalender – kavaliersmode.de</title>
<link href="https://fonts.googleapis.com/css2?family=Arimo:wght@400;700&family=Tinos:wght@400;700&display=swap" rel="stylesheet">
<style>
:root{
  --night:#0b2b57;
  --nav:#062249;
  --white:#ffffff;
  --ink:#1f3b73;
  --accent:#c9d23a;
  --gold:#d8b64a;
  --door:#1f4f8e;
  --line:#c9ccd2;
  --muted:#8a8f98;
  --social:#4aa3d6;
}
*{box-sizing:border-box;margin:0;padding:0}
html,body{width:969px;height:1200px;overflow:hidden}
body{background:var(--night);font-family:"Arimo",Arial,sans-serif;position:relative}
.page{position:absolute;left:112px;top:0;width:745px;height:1200px}
.topbar{height:43px;background:var(--white);position:relative}
.brand{position:absolute;left:8px;top:9px;display:flex;align-items:center;gap:6px;font-weight:700;font-size:20px;color:var(--night)}
.brand i{width:18px;height:18px;border-radius:50%;background:var(--night);display:block}
.perks{position:absolute;left:440px;top:-14px;width:96px;height:56px;border-radius:50%;background:#e6ebf2;font-size:8px;color:var(--ink);text-align:center;padding-top:16px;line-height:11px}
.hotline{position:absolute;right:8px;top:11px;text-align:right;font-size:9px;color:#4b3fa8;line-height:13px}
.nav{height:19px;background:var(--nav);display:flex;font-size:9px;color:var(--white);align-items:center}
.nav .all{width:108px;padding-left:8px;color:var(--accent)}
.nav a{padding:0 7px;border-right:1px solid #4f6a93;line-height:19px;color:var(--white);text-decoration:none}
.nav .gap{flex:1}
.nav .cart{color:var(--accent);border:0}
.sidebar{position:absolute;left:0;top:62px;width:108px;padding:8px 0 0 9px;font-size:10.5px;line-height:15.6px;color:var(--white)}
.content{position:absolute;left:108px;top:62px;width:637px;height:1086px;background:var(--white)}
.title{position:absolute;left:11px;top:4px;font-family:"Tinos",serif;font-weight:400;font-size:34px;color:var(--night)}
.follow{position:absolute;left:462px;top:10px;width:86px;font-size:9px;color:var(--social);font-weight:700;line-height:11px;text-align:right}
.like{position:absolute;left:555px;top:14px;width:70px;height:16px;border:1px solid #b9bec7;font-size:9px;color:#333;padding:2px 0 0 18px;background:#f2f3f5}
.like::before{content:"";position:absolute;left:4px;top:3px;width:9px;height:9px;background:#5a6f9c}
.intro{position:absolute;left:11px;top:49px;width:415px;font-size:10.5px;font-weight:700;color:var(--ink);line-height:12.5px}
.intro p+p{margin-top:10px}
.calendar{position:absolute;left:11px;top:110px;width:614px;height:371px;background:radial-gradient(ellipse at 48% 60%,#3d7ad0 0%,#1c58a8 40%,#0f3f86 100%);border:1px solid #0a2f66}
.doors{position:absolute;left:26px;top:12px;display:grid;grid-template-columns:repeat(6,67px);column-gap:35px;row-gap:29px}
.door{width:67px;height:66px;border:2px solid var(--gold);border-radius:5px;background:linear-gradient(#3566a6,var(--door));display:flex;align-items:center;justify-content:center;font-family:"Tinos",serif;font-size:44px;color:var(--white)}
.door.opened{opacity:.6}
.door.today{background:linear-gradient(#fff6b8,#e3c457);color:#b58a1b;font-weight:700}
.raffle{position:absolute;left:11px;top:489px;width:614px;height:64px;background:linear-gradient(90deg,#0f3a7a,#2c6bbd 60%,#1a4d92);color:var(--white);font-family:"Tinos",serif;font-size:22px;line-height:24px;padding:7px 10px}
.slots{position:absolute;left:13px;top:564px;display:grid;grid-template-columns:301px 301px;column-gap:10px;row-gap:8px}
.slot{position:relative;height:212px;border:1px solid var(--line)}
.slot svg{position:absolute;inset:0}
.slot span{position:absolute;left:0;right:0;top:50%;transform:translateY(-50%);text-align:center;font-size:9px;color:var(--muted);line-height:11px}
.foot-info{position:absolute;left:0;top:1018px;width:637px;border-top:1px solid #e1e3e7;padding:10px 0 0 10px;display:flex;gap:20px}
.foot-brand{font-weight:700;font-size:14px;color:var(--night);width:130px;padding-top:8px}
.foot-list{font-size:9px;color:var(--muted);line-height:14px}
.foot-list b{color:var(--ink);font-size:10px}
.footer{position:absolute;left:108px;top:1148px;width:637px;height:52px;color:var(--white);padding:8px 4px;font-size:9px;line-height:14px}
.footer b{margin-right:14px}
.footer .copy{position:absolute;right:8px;top:8px}
</style>
</head>
<body>
<div class="page">
  <header class="topbar">
    <div class="brand"><i></i>kavaliersmode.de</div>
    <div class="perks">· keine Versandkosten<br>· 180 aktuelle<br>Top-Marken</div>
    <div class="hotline">GEBÜHRENFREIE HERRENMODEBERATUNG<br>Tel: 0800 / 482 17 50 | Mo-Fr: 08:00 - 18:00</div>
  </header>
  <nav class="nav">
    <span class="all">GESAMTAUSWAHL</span>
    <a>HOME</a><a>NEU</a><a>SALE</a><a>KONTAKT</a><a>BLOG</a><a>HERRENMODE - HANDBUCH</a>
    <span class="gap"></span>
    <a>MERKZETTEL</a><a>IHR KONTO</a><a class="cart">Einkaufskorb</a>
  </nav>
  <aside class="sidebar">
    Accessoires<br>Anzüge / Sakkos<br>Gürtel<br>Hemden<br>Hosen<br>Jacken / Mäntel<br>Jeans<br>Krawatten<br>Nachtwäsche / Bad<br>Polos<br>Pullover<br>Schuhe<br>Socken<br>Sportswear / Sport<br>T-Shirts<br>Unterwäsche
  </aside>
  <main class="content">
    <h1 class="title">Online Adventskalender</h1>
    <div class="follow">folge uns auf<br>Zwitscherdienst</div>
    <div class="like">Gefällt mir</div>
    <div class="intro">
      <p>In unserem Online Adventskalender warten jeden Tag eine neue Weihnachts-Überraschung auf Sie - unter anderem Beispiel 1, Beispiel 2 oder Beispiel 3. Zudem eine Verlosung von Preisen unter allen Teilnehmern!</p>
      <p>Also mitraten und gewinnen!</p>
    </div>
    <section class="calendar" role="img" aria-label="Winterliche Illustration mit leuchtendem Sternen-Tannenbaum auf blauem Grund">
      <div class="doors">
        <div class="door opened">1</div><div class="door today">2</div><div class="door">3</div><div class="door">4</div><div class="door">5</div><div class="door">6</div>
        <div class="door">7</div><div class="door">8</div><div class="door">9</div><div class="door">10</div><div class="door">11</div><div class="door">12</div>
        <div class="door">13</div><div class="door">14</div><div class="door">15</div><div class="door">16</div><div class="door">17</div><div class="door">18</div>
        <div class="door">19</div><div class="door">20</div><div class="door">21</div><div class="door">22</div><div class="door">23</div><div class="door">24</div>
      </div>
    </section>
    <div class="raffle" role="img" aria-label="Gewinnbanner mit silberner Geschenkschleife">Und unter allen Teilnehmern verlosen wir:<br>Gutscheine im Wert von jeweils 100 Euro</div>
    <div class="slots">
      <div class="slot"><svg width="301" height="212"><line x1="0" y1="0" x2="301" y2="212" stroke="#c9ccd2"/><line x1="301" y1="0" x2="0" y2="212" stroke="#c9ccd2"/></svg><span>ZWITSCHER-STREAM</span></div>
      <div class="slot"><svg width="301" height="212"><line x1="0" y1="0" x2="301" y2="212" stroke="#c9ccd2"/><line x1="301" y1="0" x2="0" y2="212" stroke="#c9ccd2"/></svg><span>FREUNDESNETZ LIKE-BOX</span></div>
      <div class="slot"><svg width="301" height="212"><line x1="0" y1="0" x2="301" y2="212" stroke="#c9ccd2"/><line x1="301" y1="0" x2="0" y2="212" stroke="#c9ccd2"/></svg><span>FORMULAR ZUR WEITEREMPFEHLUNG<br>PER E-MAIL</span></div>
      <div class="slot"><svg width="301" height="212"><line x1="0" y1="0" x2="301" y2="212" stroke="#c9ccd2"/><line x1="301" y1="0" x2="0" y2="212" stroke="#c9ccd2"/></svg><span>TEXT RECHTLICHES / DISCLAIMER</span></div>
    </div>
    <div class="foot-info">
      <div class="foot-brand">kavaliersmode.de</div>
      <div class="foot-list"><b>Herrenmode im Online Shop für Herren</b><br>· Kostenloser Versand<br>· 30 Tage Rückgaberecht<br>· Günstig kaufen</div>
    </div>
  </main>
  <footer class="footer">
    <b>UNSERE AGB</b><b>DATENSCHUTZBESTIMMUNG</b><b>IMPRESSUM</b><br>
    HERRENMODE &nbsp;· ALLE MARKEN &nbsp;· ALLE KATEGORIEN &nbsp;· AKTUELLE MÄNNERMODE
    <span class="copy">© seit 1997 Vellmar AG</span>
  </footer>
</div>
</body>
</html>
```